Monthly Planner & To Do List on dry erase magnetic whiteboard

I'm after 2 x designs for magnetic whiteboards.
1. 17 x 13 inches is a monthly planner. Dates and month can be written in each month and then wiped off and re-written for the next month.
2. 6 x 4 inches - to do list however I don't want this to say To Do on it but will have lines to write on and possibly bullet points to check off.
I have attached below samples of other products (the ones I like the most are the first two - 9.19.52 and 9.20.34). I actually don't like the design of the others but just show them here as an example for layout purposes.
I want something that is modern, slick, simple yet stylish which is what my brand is representative of - smart, modern, organised. It will be printed onto a white board and I only want the print to be in black, no grey shading. I need a more modern font and don't like any of the swirly parts. Just clean and simple but slick.
I would like the size of the day squares to be as large as possible to fit writing in them and also for a section somewhere on the page for additional notes.

• Old style fonts, cartoon style or childish.

```html
<!DOCTYPE html>
<html lang="en">
<head>
<meta charset="utf-8">
<title>Monthly Calendar + List Boards</title>
<link rel="stylesheet" href="https://fonts.googleapis.com/css2?family=Share+Tech+Mono&display=swap">
<style>
  :root {
    --backdrop: #ededed;
    --board: #ffffff;
    --ink: #000000;
    --shadow: rgba(0, 0, 0, 0.28);
  }
  html, body {
    margin: 0;
    padding: 0;
    width: 1200px;
    height: 1000px;
    overflow: hidden;
    background: var(--backdrop);
  }
  .stage {
    display: block;
    width: 1200px;
    height: 1000px;
  }
  .board-shadow { fill: var(--shadow); }
  .board-frame { fill: var(--board); stroke: var(--ink); stroke-width: 4; }
  .grid-solid { fill: none; stroke: var(--ink); stroke-width: 1; }
  .grid-dotted { fill: none; stroke: var(--ink); stroke-width: 1; stroke-dasharray: 1 2; }
  .label-box { fill: var(--board); stroke: var(--ink); stroke-width: 1; }
  .label-box-dotted { fill: var(--board); stroke: var(--ink); stroke-width: 1; stroke-dasharray: 1 2; }
  .label-text {
    font-family: "Share Tech Mono", monospace;
    font-size: 12px;
    fill: var(--ink);
    text-anchor: middle;
  }
  .label-text-notes { font-style: italic; }
  .checkbox { fill: var(--board); stroke: var(--ink); stroke-width: 1; }
</style>
</head>
<body>
<svg class="stage" viewBox="0 0 1200 1000" xmlns="http://www.w3.org/2000/svg">

  <!-- Monthly planner board -->
  <g class="monthly-planner">
    <rect class="board-shadow" x="52" y="52" width="806" height="618"/>
    <rect class="board-frame" x="38" y="38" width="804" height="616"/>

    <path class="grid-solid" d="M49 97H138M49 97V642M49 206H138M49 315H138M49 424H138M49 533H138M49 642H138"/>
    <path class="grid-solid" d="M146 97H235M146 97V642M146 206H235M146 315H235M146 424H235M146 533H235M146 642H235"/>
    <path class="grid-solid" d="M243 97H331M243 97V642M243 206H331M243 315H331M243 424H331M243 533H331M243 642H331"/>
    <path class="grid-solid" d="M340 97H428M340 97V642M340 206H428M340 315H428M340 424H428M340 533H428M340 642H428"/>
    <path class="grid-solid" d="M436 97H525M436 97V642M436 206H525M436 315H525M436 424H525M436 533H525M436 642H525"/>
    <path class="grid-dotted" d="M534 97H622M534 97V642M534 206H622M534 315H622M534 424H622M534 533H622M534 642H622"/>
    <path class="grid-dotted" d="M630 97H719M630 97V642M630 206H719M630 315H719M630 424H719M630 533H719M630 642H719"/>

    <g class="day-labels">
      <rect class="label-box" x="67" y="88" width="52" height="17"/>
      <text class="label-text" x="93" y="101">Monday</text>
      <rect class="label-box" x="160" y="88" width="60" height="17"/>
      <text class="label-text" x="190" y="101">Tuesday</text>
      <rect class="label-box" x="250" y="88" width="74" height="17"/>
      <text class="label-text" x="287" y="101">Wednesday</text>
      <rect class="label-box" x="350" y="88" width="66" height="17"/>
      <text class="label-text" x="383" y="101">Thursday</text>
      <rect class="label-box" x="455" y="88" width="50" height="17"/>
      <text class="label-text" x="480" y="101">Friday</text>
      <rect class="label-box-dotted" x="545" y="88" width="66" height="17"/>
      <text class="label-text" x="578" y="101">Saturday</text>
      <rect class="label-box-dotted" x="649" y="88" width="52" height="17"/>
      <text class="label-text" x="675" y="101">Sunday</text>
    </g>

    <g class="notes-column">
      <rect class="grid-solid" x="727" y="97" width="105" height="545"/>
      <rect class="grid-solid" x="730" y="100" width="99" height="539"/>
      <rect class="label-box" x="756" y="87" width="49" height="19"/>
      <rect class="label-box" x="758" y="89" width="45" height="15"/>
      <text class="label-text label-text-notes" x="780.5" y="101">Notes</text>
    </g>
  </g>

  <!-- List board -->
  <g class="list-board">
    <rect class="board-shadow" x="883" y="52" width="296" height="437"/>
    <rect class="board-frame" x="869" y="38" width="294" height="435"/>

    <path class="grid-solid" d="M887 57H1146M887 57V340M887 85.3H1146M887 113.6H1146M887 141.9H1146M887 170.2H1146M887 198.5H1146M887 226.8H1146M887 255.1H1146M887 283.4H1146M887 311.7H1146M887 340H1146"/>

    <g class="checkboxes">
      <rect class="checkbox" x="892" y="63" width="15" height="15"/>
      <rect class="checkbox" x="892" y="91.3" width="15" height="15"/>
      <rect class="checkbox" x="892" y="119.6" width="15" height="15"/>
      <rect class="checkbox" x="892" y="147.9" width="15" height="15"/>
      <rect class="checkbox" x="892" y="176.2" width="15" height="15"/>
      <rect class="checkbox" x="892" y="204.5" width="15" height="15"/>
      <rect class="checkbox" x="892" y="232.8" width="15" height="15"/>
      <rect class="checkbox" x="892" y="261.1" width="15" height="15"/>
      <rect class="checkbox" x="892" y="289.4" width="15" height="15"/>
      <rect class="checkbox" x="892" y="317.7" width="15" height="15"/>
    </g>

    <g class="list-notes">
      <rect class="grid-solid" x="887" y="359" width="259" height="98"/>
      <rect class="grid-solid" x="890" y="362" width="253" height="92"/>
      <rect class="label-box" x="992" y="352" width="48" height="18"/>
      <rect class="label-box" x="994" y="354" width="44" height="14"/>
      <text class="label-text label-text-notes" x="1016" y="365.5">Notes</text>
    </g>
  </g>
</svg>
</body>
</html>
```